Flyer
Der Flyer ist super geworden. Vielen Dank! :-)
Zielgruppe
Wir sind Hersteller von Unterkonstruktion für PV-Anlagen. Unsere Zielgruppe sind Monteure oder Firmen die PV-Anlagen verbauen.
Aufgabenstellung
Ich hätte gerne einen Slogan wie Bestpreisgarantie. Oder: Unterkonstruktionen in bester Qualität – zum besten Preis
Oder Sie haben selbst Vorschläge; Wenn möglich können Sie gerne die Bilder von der pptx Datei nehmen. Wir haben auf den Clip unter der Hammerkopfschraube ein Patent (liegt bei), dieser Clip ist ein deutlicher Vorteil bei der Verbauung, damit sich die Hammerkopfschraube beim Verbauen nicht verdreht.
Unsere Adresse sollte noch auf den Flyer:
KD Lumatrix Werke GmbH, Falkenhainweg 14, 80417 München
Fon: 089 518 327 40 Mail: info@kdlumatrixwerke.com
Website: www.kdlumatrixwerke.com

```html
<!DOCTYPE html>
<html lang="de">
<head>
<meta charset="utf-8">
<title>KD Lumatrix Werke – Flyer</title>
<link href="https://fonts.googleapis.com/css2?family=Kanit:wght@600;700&family=Poppins:wght@300;400;500&family=Arimo:wght@700&display=swap" rel="stylesheet">
<style>
:root{
  --stage:#4b4b4b;
  --blue:#3f62a3;
  --navy:#1f3f7c;
  --sky:#7e9ad0;
  --pale:#edf1f9;
  --white:#ffffff;
  --ink:#2b2b2b;
  --label:#ffffff;
}
*{margin:0;padding:0;box-sizing:border-box}
html,body{width:825px;height:1200px;overflow:hidden;background:var(--stage)}
.sheet{position:relative;width:825px;height:1200px;font-family:"Poppins",sans-serif;color:var(--ink)}
.abs{position:absolute}
.view-label{position:absolute;font-family:"Arimo",sans-serif;font-weight:700;font-size:19px;color:var(--label)}
.photo{position:absolute}
.photo-roof-panels{background:linear-gradient(160deg,#b9bdc7 0%,#5e6c95 40%,#3a4a7a 70%,#8a90a8 100%)}
.photo-roof-tiles{background:linear-gradient(115deg,#c8ccd2 0%,#9aa2ae 25%,#b4543a 45%,#8e3f2c 55%,#434d72 70%,#6c7598 100%)}
.photo-worker{background:linear-gradient(150deg,#c7ccd6 0%,#6f7fa6 45%,#33456f 80%,#5a6788 100%)}
.drawing{position:absolute;background:linear-gradient(135deg,#3d3d40 0%,#5a5a5e 40%,#c9a877 70%,#e6d2ae 100%)}
.pale{background:var(--pale)}
.white{background:var(--white)}
.blue{background:var(--blue)}
.feature{position:absolute}
.feature svg{position:absolute;left:0;top:0}
.feature h3{position:absolute;font-family:"Kanit",sans-serif;font-weight:600;font-size:11.5px;color:var(--blue);white-space:nowrap;line-height:1}
.feature p{position:absolute;font-size:8.3px;font-weight:300;line-height:11.8px;color:var(--ink)}
.feature.on-blue h3{color:var(--white)}
.feature.on-blue p{color:#dfe6f4}
.brand-box{position:absolute;background:var(--white);text-align:center}
.brand-mark{display:block;margin:0 auto;background:var(--navy)}
.brand-name{font-family:"Poppins",sans-serif;font-weight:400;color:var(--navy);white-space:nowrap;letter-spacing:.5px}
.brand-claim{font-size:8.4px;font-weight:300;color:var(--blue);line-height:11px}
.guarantee{position:absolute;color:var(--white)}
.guarantee .band{position:absolute;background:var(--blue);clip-path:polygon(14% 0,100% 0,100% 100%,0 100%)}
.guarantee .band h2{position:absolute;font-family:"Kanit",sans-serif;font-weight:700;font-size:20px;line-height:20px;letter-spacing:.4px}
.guarantee .sub{position:absolute;background:var(--sky);clip-path:polygon(12% 0,100% 0,100% 100%,0 100%)}
.guarantee .sub p{position:absolute;font-size:8.4px;font-weight:500;line-height:11px}
.address{position:absolute;background:var(--white);padding:8px 0 0 13px}
.address .brand-name{font-size:7.4px;margin-left:0}
.address p{font-size:6.3px;line-height:10px;color:var(--navy)}
.address strong{font-weight:500}
.legend{position:absolute;list-style:none;font-size:7.4px;font-weight:500;color:var(--ink)}
.legend li{display:flex;align-items:center;height:17px}
.legend i{display:inline-block;width:7px;height:7px;border-radius:50%;margin-right:10px}
.certs{position:absolute;display:flex;gap:10px;align-items:center}
.certs span{display:block;width:16px;height:16px;border-radius:50%;background:#c9d0dc}
.cta{position:absolute;color:var(--white)}
.cta h2{font-family:"Kanit",sans-serif;font-weight:700;font-size:20px;line-height:21px;letter-spacing:.3px}
.cta p{font-size:8.3px;font-weight:300;line-height:11.8px;margin-top:12px}
.cta .contact{font-weight:500;margin-top:4px}
.flap{position:absolute;box-shadow:-6px 4px 12px rgba(0,0,0,.35)}
</style>
</head>
<body>
<div class="sheet">

  <!-- Row 1 -->
  <div class="view-label" style="left:88px;top:30px">Klappe</div>
  <div class="view-label" style="left:327px;top:30px">Rückseite</div>
  <div class="view-label" style="left:545px;top:30px">Vorderseite</div>

  <div class="photo photo-worker" style="left:45px;top:67px;width:228px;height:166px" role="img" aria-label="Foto: Monteur schraubt Solarmodul auf dem Dach fest"></div>
  <div class="abs pale" style="left:45px;top:233px;width:228px;height:161px"></div>
  <div class="feature" style="left:76px;top:261px;width:190px;height:100px">
    <svg width="25" height="25" viewBox="0 0 25 25"><circle cx="12.5" cy="12.5" r="11.3" fill="none" stroke="var(--blue)" stroke-width="1.6"/><path d="M8.5 16.5 L16 9 M10 9 H16 V15" fill="none" stroke="var(--blue)" stroke-width="1.6"/></svg>
    <h3 style="left:33px;top:0">Preisvorteil</h3>
    <p style="left:33px;top:15px;width:130px">Sehr günstige Einkaufspreise und hervorragende Qualität bei den Unterkonstruktionssystemen durch langjährige Erfahrung mit Herstellern und Lieferanten aus dem DACH-Gebiet.</p>
  </div>

  <div class="photo photo-roof-tiles" style="left:273px;top:67px;width:469px;height:327px" role="img" aria-label="Foto: Ziegeldach mit Solarmodulen und Dachfenster"></div>

  <div class="address" style="left:332px;top:315px;width:122px;height:79px">
    <span class="brand-mark" style="width:14px;height:10px;margin:0 0 6px 36px"></span>
    <div class="brand-name" style="margin-bottom:4px">KD LUMATRIX WERKE</div>
    <p><strong>KD Lumatrix Werke GmbH,</strong><br>Falkenhainweg 14, 80417 München<br>www.kdlumatrixwerke.com</p>
  </div>

  <div class="brand-box" style="left:544px;top:67px;width:162px;height:107px;padding-top:14px">
    <span class="brand-mark" style="width:30px;height:22px;margin-bottom:8px"></span>
    <div class="brand-name" style="font-size:12.5px">KD LUMATRIX WERKE</div>
    <p class="brand-claim" style="margin-top:8px">Unterkonstruktionen für<br>eine standhafte Zukunft!</p>
  </div>

  <div class="guarantee" style="left:582px;top:233px;width:160px;height:116px">
    <div class="band" style="left:0;top:0;width:160px;height:68px">
      <h2 style="left:42px;top:14px">BESTPREIS-<br>GARANTIE</h2>
    </div>
    <div class="sub" style="left:18px;top:68px;width:142px;height:48px">
      <p style="left:38px;top:8px">Unterkonstruktionen<br>in bester Qualität –<br>zum besten Preis</p>
    </div>
  </div>

  <!-- Row 2 -->
  <div class="view-label" style="left:88px;top:413px">Innen</div>
  <div class="view-label" style="left:327px;top:413px">Innen</div>
  <div class="view-label" style="left:545px;top:413px">Klappe offen</div>

  <div class="photo photo-worker" style="left:45px;top:450px;width:236px;height:164px" role="img" aria-label="Foto: Techniker mit Laptop und Messgerät auf Solarmodulen"></div>
  <div class="abs blue" style="left:45px;top:614px;width:236px;height:163px"></div>
  <div class="feature on-blue" style="left:79px;top:642px;width:200px;height:100px">
    <svg width="25" height="25" viewBox="0 0 25 25"><circle cx="12.5" cy="12.5" r="11.3" fill="none" stroke="#fff" stroke-width="1.6"/><path d="M12.5 7 V18 M7 12.5 H18" stroke="#fff" stroke-width="1.8"/></svg>
    <h3 style="left:33px;top:0">Zuverlässige Konstruktionen</h3>
    <p style="left:33px;top:15px;width:140px">Die 100%ige Liefertreue und Qualität wird durch die langjährige Produktionserfahrung und ständige Überwachung der Lieferanten sichergestellt.</p>
  </div>

  <div class="abs pale" style="left:281px;top:450px;width:234px;height:164px"></div>
  <div class="feature" style="left:318px;top:477px;width:190px;height:100px">
    <svg width="25" height="25" viewBox="0 0 25 25"><path d="M8 3.5 A10.5 10.5 0 1 0 22.5 14" fill="none" stroke="var(--blue)" stroke-width="1.6"/><circle cx="13.5" cy="2.5" r="1" fill="var(--blue)"/><circle cx="18" cy="4" r="1" fill="var(--blue)"/><circle cx="21" cy="7.5" r="1" fill="var(--blue)"/></svg>
    <h3 style="left:33px;top:0">Reduzierte Montagezeit</h3>
    <p style="left:33px;top:15px;width:140px">Profilschienen und patentierte Verbindungselemente garantieren hohe Sicherheit, Flexibilität und universellen Einsatz.</p>
  </div>

  <div class="drawing" style="left:281px;top:614px;width:180px;height:163px" role="img" aria-label="Technische Zeichnung: Profilschiene mit Hammerkopf, Kunststoff-Clip und Winkel"></div>
  <div class="abs white" style="left:430px;top:614px;width:85px;height:100px"></div>
  <ul class="legend" style="left:434px;top:623px">
    <li><i style="background:#5b5b5e"></i>Profilschiene</li>
    <li><i style="background:#e21ee0"></i>Hammerkopf</li>
    <li><i style="background:#21d6dc"></i>Kuststoff-Clip</li>
    <li><i style="background:#c9a877"></i>Winkel</li>
  </ul>

  <div class="abs white" style="left:515px;top:450px;width:227px;height:164px"></div>
  <div class="feature" style="left:547px;top:477px;width:190px;height:100px">
    <svg width="25" height="25" viewBox="0 0 25 25"><circle cx="12.5" cy="12.5" r="11.3" fill="none" stroke="var(--blue)" stroke-width="1.6"/><path d="M7 12.5 L11 17 L18.5 8" fill="none" stroke="var(--blue)" stroke-width="1.8"/></svg>
    <h3 style="left:33px;top:0">Sicherheit</h3>
    <p style="left:33px;top:15px;width:140px">Unser Unternehmen, die Produktion und Materialien sind auditiert und zertifiziert.</p>
  </div>
  <div class="certs" style="left:548px;top:553px">
    <span style="width:24px;height:10px;border-radius:5px"></span><span></span><span style="width:10px;height:10px"></span><span></span><span></span><span style="background:#e0b44a"></span>
  </div>

  <div class="abs blue" style="left:515px;top:614px;width:227px;height:163px"></div>
  <div class="cta" style="left:545px;top:640px;width:190px">
    <h2>JETZT BERATEN<br>LASSEN!</h2>
    <p>Unser Team informiert sie gerne<br>über die Vorteile unserer Syteme.</p>
    <p class="contact">089 518 327 40<br>info@kdlumatrixwerke.com</p>
  </div>

  <!-- Row 3 -->
  <div class="view-label" style="left:82px;top:804px">Innen</div>
  <div class="view-label" style="left:301px;top:804px">Klappe geschlossen</div>
  <div class="view-label" style="left:587px;top:804px">Vorne geschlossen</div>

  <div class="photo photo-worker" style="left:45px;top:841px;width:236px;height:164px" role="img" aria-label="Foto: Techniker mit Laptop und Messgerät auf Solarmodulen"></div>
  <div class="abs blue" style="left:45px;top:1005px;width:236px;height:163px"></div>
  <div class="feature on-blue" style="left:79px;top:1033px;width:200px;height:100px">
    <svg width="25" height="25" viewBox="0 0 25 25"><circle cx="12.5" cy="12.5" r="11.3" fill="none" stroke="#fff" stroke-width="1.6"/><path d="M12.5 7 V18 M7 12.5 H18" stroke="#fff" stroke-width="1.8"/></svg>
    <h3 style="left:33px;top:0">Zuverlässige Konstruktionen</h3>
    <p style="left:33px;top:15px;width:140px">Die 100%ige Liefertreue und Qualität wird durch die langjährige Produktionserfahrung und ständige Überwachung der Lieferanten sichergestellt.</p>
  </div>

  <div class="abs pale" style="left:281px;top:841px;width:40px;height:164px"></div>
  <div class="drawing" style="left:281px;top:1005px;width:40px;height:163px" role="img" aria-label="Technische Zeichnung: Profilschiene, teilweise verdeckt"></div>

  <div class="flap" style="left:316px;top:826px;width:199px;height:342px">
    <div class="photo photo-worker" style="left:0;top:0;width:199px;height:176px" role="img" aria-label="Foto: Monteur schraubt Solarmodul auf dem Dach fest"></div>
    <div class="abs pale" style="left:0;top:176px;width:199px;height:166px"></div>
    <div class="feature" style="left:28px;top:196px;width:170px;height:100px">
      <svg width="22" height="22" viewBox="0 0 25 25"><circle cx="12.5" cy="12.5" r="11.3" fill="none" stroke="var(--blue)" stroke-width="1.6"/><path d="M8.5 16.5 L16 9 M10 9 H16 V15" fill="none" stroke="var(--blue)" stroke-width="1.6"/></svg>
      <h3 style="left:29px;top:0">Preisvorteil</h3>
      <p style="left:29px;top:15px;width:112px">Sehr günstige Einkaufspreise und hervorragende Qualität bei den Unterkonstruktionssystemen durch langjährige Erfahrung mit Herstellern und Lieferanten aus dem DACH-Gebiet.</p>
    </div>
  </div>

  <div class="photo photo-roof-panels" style="left:565px;top:841px;width:227px;height:327px" role="img" aria-label="Foto: Solarmodule auf einem Ziegeldach"></div>
  <div class="brand-box" style="left:593px;top:841px;width:163px;height:107px;padding-top:14px">
    <span class="brand-mark" style="width:30px;height:22px;margin-bottom:8px"></span>
    <div class="brand-name" style="font-size:12.5px">KD LUMATRIX WERKE</div>
    <p class="brand-claim" style="margin-top:8px">Unterkonstruktionen für<br>eine standhafte Zukunft!</p>
  </div>
  <div class="guarantee" style="left:631px;top:1007px;width:161px;height:116px">
    <div class="band" style="left:0;top:0;width:161px;height:68px">
      <h2 style="left:42px;top:14px">BESTPREIS-<br>GARANTIE</h2>
    </div>
    <div class="sub" style="left:18px;top:68px;width:143px;height:48px">
      <p style="left:38px;top:8px">Unterkonstruktionen<br>in bester Qualität –<br>zum besten Preis</p>
    </div>
  </div>

</div>
</body>
</html>
```